Need a business card design. I am a Self Empowerment Life Coach.

A Life Coach is - a professional relationship designed to enhance an individual's ability to focus, make effective changes, develop oneself, achieve desired goals and maximize success in life. Coaching is about getting the very best out of someone and enabling them to make decisions that will improve their life. It is a unique way to help people look at where they are now and where they would like to be, and helps bridge the gap.

Bright Path Coaching is motivational, inspiring, positive, exciting and action driven. By raising awareness and encouraging others to take responsibility for their life, coaching can help people rise to their challenge and go further than you ever thought possible.

Industry/Entity Type

Business

Other font styles liked:
• Bookman Old Style

Requirements
Must have
• Marla Thorncastle, QTV-AR
• Self Empowerment Coach
• 318.557.6021
• mt@thebloomingpathcoach.example
• The attached logo
Nice to have
• I would like to see some designs portrait and some landscape

```html
<!DOCTYPE html>
<html lang="en">
<head>
<meta charset="utf-8">
<title>Bright Path Coaching – Business Card</title>
<link rel="stylesheet" href="https://fonts.googleapis.com/css2?family=Libre+Baskerville:wght@400;700&display=swap">
<style>
  :root {
    --bg: #ece8e1;
    --paper: #ffffff;
    --paper-shade: #eef0f3;
    --navy: #1f4f9a;
    --navy-deep: #17407f;
    --cyan: #2bb3de;
    --yellow: #f3d21b;
    --ink: #2a3550;
    --ink-soft: #5c6b86;
  }
  * { box-sizing: border-box; margin: 0; padding: 0; }
  html, body {
    width: 1200px; height: 600px; overflow: hidden;
    background: var(--bg);
    font-family: "Libre Baskerville", "Bookman Old Style", serif;
  }
  .stage {
    width: 1200px; height: 600px;
    display: flex; align-items: center; justify-content: center; gap: 60px;
  }
  .card {
    position: relative;
    width: 520px; height: 297px;
    border-radius: 16px;
    overflow: hidden;
    background: linear-gradient(160deg, var(--paper) 55%, var(--paper-shade));
    box-shadow: 0 6px 18px rgba(0,0,0,.15);
  }
  .card-art { position: absolute; inset: 0; }

  /* front */
  .name-tab {
    position: absolute; left: 0; top: 34px;
    width: 330px; height: 74px;
    background: var(--yellow);
    border-radius: 0 37px 37px 0;
    padding: 13px 0 0 26px;
  }
  .name {
    font-size: 20px; color: var(--ink); letter-spacing: .2px;
  }
  .title {
    font-size: 14px; color: var(--ink-soft); margin-top: 5px;
  }
  .brand {
    position: absolute; display: flex; align-items: center; gap: 8px;
  }
  .brand-dot {
    width: 18px; height: 18px; border-radius: 50%; background: var(--yellow);
    flex: none;
  }
  .brand-name {
    font-size: 15px; font-weight: 700; color: var(--navy); line-height: 1.15;
  }
  .card-front .brand { right: 26px; top: 44px; }
  .contact {
    position: absolute; left: 246px; bottom: 24px;
    list-style: none; color: #fff; font-size: 11.5px;
  }
  .contact li { display: flex; align-items: center; gap: 8px; margin-top: 6px; white-space: nowrap; }
  .contact svg { width: 11px; height: 11px; flex: none; }

  /* back */
  .card-back .brand {
    left: 50%; top: 92px; transform: translateX(-50%);
  }
  .card-back .brand-dot { width: 26px; height: 26px; }
  .card-back .brand-name { font-size: 24px; }
</style>
</head>
<body>
<main class="stage">

  <section class="card card-front" aria-label="Business card front">
    <svg class="card-art" viewBox="0 0 520 297" aria-hidden="true">
      <polygon points="130,297 230,150 520,92 520,112 244,168 152,297" fill="var(--cyan)"/>
      <polygon points="156,297 248,172 520,116 520,297" fill="var(--navy)"/>
      <polygon points="440,297 520,230 520,297" fill="var(--navy-deep)" opacity=".6"/>
    </svg>

    <div class="name-tab">
      <p class="name">Marla Thorncastle, QTV-AR</p>
      <p class="title">Self Empowerment Coach</p>
    </div>

    <div class="brand">
      <span class="brand-dot"></span>
      <span class="brand-name">Bright Path<br>Coaching</span>
    </div>

    <ul class="contact">
      <li>
        <svg viewBox="0 0 12 12"><path d="M2.5 1h2l1 3-1.5 1a7 7 0 0 0 3 3l1-1.5 3 1v2c0 .6-.5 1-1 1A10 10 0 0 1 1.5 2c0-.5.4-1 1-1z" fill="#fff"/></svg>
        318.557.6021
      </li>
      <li>
        <svg viewBox="0 0 12 12"><rect x="1" y="2.5" width="10" height="7" fill="none" stroke="#fff" stroke-width="1.2"/><path d="M1 3l5 3.5L11 3" fill="none" stroke="#fff" stroke-width="1.2"/></svg>
        mt@thebloomingpathcoach.example
      </li>
      <li>
        <svg viewBox="0 0 12 12"><circle cx="6" cy="6" r="4.8" fill="none" stroke="#fff" stroke-width="1.1"/><path d="M1.2 6h9.6M6 1.2c-2.4 2.8-2.4 6.8 0 9.6M6 1.2c2.4 2.8 2.4 6.8 0 9.6" fill="none" stroke="#fff" stroke-width="1"/></svg>
        www.thebloomingpathcoach.example
      </li>
    </ul>
  </section>

  <section class="card card-back" aria-label="Business card back">
    <svg class="card-art" viewBox="0 0 520 297" aria-hidden="true">
      <polygon points="0,236 520,262 520,270 0,246" fill="var(--cyan)"/>
      <polygon points="0,250 520,274 520,297 0,297" fill="var(--navy)"/>
    </svg>
    <div class="brand">
      <span class="brand-dot"></span>
      <span class="brand-name">Bright Path Coaching</span>
    </div>
  </section>

</main>
</body>
</html>
```